Marbeck Partners Exit Plan business consultant web site

This website is for a consulting business that helps other businesses with exit plans. Essentially, assists them with the sale of their business. This website should be very professional, almost with a wall street look. I would like a very attractive image on the homepage. Perhaps something that denotes success. Perhaps a picture of palm trees and a beach? I will leave it to you for interpretation.

Across the screen I would like the words "Does your business have an exit plan?"

Below that it should read the following:
Let us help you with a completely impartial, no obligation assessment (button with link to the contact page)

Also, please use logo in a prominent place on the website so it's easily seen.

Target Market(s)

Males 40+

Coding

Coded - Design and coding required

Number of Pages Required

5+ page

Colors

Designer to choose colors to be used in the design.

Requirements
Must have
• The tabs for the homepage on the top should be:
• 1. About us
• 2. Services
• 3. Industries
• 4. Our success
• 5. Contact
Nice to have
• Clean, professional image.
• Please put FB, News Feed, Linked In - logos at bottom.
• Here are two examples of a website to give you an idea:
• https://blog.trevanquill.com/library/why-every-business-owner-should-have-an-exit-plan
Should not have
• nothing whimsical or cartoon like

```html
<!DOCTYPE html>
<html lang="en">
<head>
<meta charset="utf-8">
<title>Marbeck Partners — Exit Planning Advisors</title>
<link rel="stylesheet" href="https://fonts.googleapis.com/css2?family=Poppins:ital,wght@0,400;0,500;0,600;0,700;0,800;1,400&family=Caveat:wght@500&display=swap">
<style>
:root{
  --backdrop:#eef0f2;
  --red:#e84c56;
  --red-dark:#d63e48;
  --navy:#1d2132;
  --navy-2:#2a2f42;
  --ink:#1b1d24;
  --muted:#8b8f99;
  --gray-bg:#f0f0f0;
  --field:#ececec;
  --yellow:#f7e14a;
  --white:#ffffff;
}
*{box-sizing:border-box;margin:0;padding:0}
html,body{width:1200px;height:2400px;overflow:hidden;background:var(--backdrop)}
body{font-family:"Poppins",sans-serif;color:var(--ink)}
.page{position:absolute;left:375px;top:0;width:1200px;height:6400px;transform:scale(.375);transform-origin:0 0;background:var(--white);box-shadow:0 0 90px rgba(0,0,0,.25)}
section,header,nav,footer{position:relative;width:1200px;overflow:visible}
.abs{position:absolute}
.photo{position:absolute}
.eyebrow{position:absolute;font-family:"Caveat",cursive;font-size:15px;color:var(--red);white-space:nowrap}
.eyebrow.center{left:0;width:1200px;text-align:center}
.mark{position:absolute;width:7px;height:7px;background:var(--red);transform:rotate(45deg)}
.mark.center{left:597px}
.heading{position:absolute;font-weight:700;font-size:33px;line-height:43px;letter-spacing:-.5px}
.heading.center{left:0;width:1200px;text-align:center}
.btn{position:absolute;display:flex;align-items:center;justify-content:center;font-size:11px;font-weight:600;border-radius:2px}
.btn.red{background:var(--red);color:var(--white)}
.btn.white{background:var(--white);color:var(--ink)}
.small{font-size:10.5px;line-height:20px;color:var(--muted)}

/* top bar */
.topbar{height:86px;background:#f4f4f4}
.brand{position:absolute;left:134px;top:22px;display:flex;align-items:center;gap:12px;font-size:17px;font-weight:500;color:var(--navy);letter-spacing:1px}
.brand-square{width:40px;height:40px;background:var(--navy)}
.contact-item{position:absolute;top:26px;display:flex;gap:10px;align-items:center}
.icon-dot{width:28px;height:28px;border-radius:50%;background:var(--red);display:flex;align-items:center;justify-content:center}
.contact-item .lab{font-size:9px;color:var(--muted);line-height:13px}
.contact-item .val{font-size:10px;font-weight:600;line-height:14px}

/* nav */
.mainnav{height:43px;background:var(--navy)}
.mainnav ul{list-style:none;position:absolute;left:383px;top:0;height:43px;display:flex;gap:30px;align-items:center}
.mainnav li{font-size:12px;color:#d8dae2}
.mainnav li.active{color:var(--red)}
.lang{position:absolute;left:906px;top:13px;display:flex;gap:8px;align-items:center;font-size:11px;color:#d8dae2}
.lang i{width:16px;height:16px;border-radius:50%;background:#c7ccd8;display:block}

/* hero */
.hero{height:541px;overflow:hidden}
.hero-photo{inset:0;background:linear-gradient(180deg,#4f7fb4 0%,#6f9cc8 26%,#2f86a6 31%,#4fb7c0 45%,#7fd0cf 62%,#b8d8cf 78%,#e0d6c6 90%,#e8ddcd 100%)}
.hero h1{position:absolute;left:0;top:14px;width:1200px;text-align:center;font-size:74px;line-height:84px;font-weight:800;color:var(--white);letter-spacing:1px;text-shadow:0 3px 8px rgba(0,0,0,.25)}
.hero .lead{position:absolute;left:0;top:190px;width:1200px;text-align:center;font-size:22px;color:var(--white);text-shadow:0 1px 4px rgba(0,0,0,.4)}
.hero .btn{left:513px;top:472px;width:174px;height:48px;font-size:19px;font-weight:500;border-radius:6px}

/* mission */
.mission{height:1284px;background:linear-gradient(180deg,var(--gray-bg) 383px,var(--white) 383px)}
.team-photo{left:228px;top:233px;width:745px;height:348px;background:linear-gradient(135deg,#6d87a6,#c4cdd6 45%,#8c98a4 70%,#dfe4ea)}
.commit-card{position:absolute;left:247px;top:453px;width:241px;height:128px;background:var(--white);padding:32px 30px}
.commit-card p{font-size:12px;font-weight:600;line-height:18px}
.commit-card span{display:block;margin-top:10px;font-size:8px;font-weight:700;color:var(--red);letter-spacing:1px}
.office-photo{left:228px;top:809px;width:338px;height:190px;background:linear-gradient(135deg,#cfd8e4,#6b7c96 55%,#a9b4c4)}
.solutions{position:absolute;left:611px;top:656px;width:362px}
.sol-head{height:48px;background:var(--red);color:var(--white);font-size:9.5px;font-weight:600;display:flex;align-items:center;padding-left:22px;gap:8px}
.sol-body{padding:16px 22px;font-size:9.5px;line-height:19px;color:var(--muted)}
.sol-row{height:46px;margin-top:10px;background:#f1f1f1;font-size:9.5px;font-weight:500;display:flex;align-items:center;padding-left:22px;gap:12px}
.sol-row b{color:var(--red);font-weight:700}
.rule{position:absolute;left:0;top:1077px;width:1200px;height:1px;background:#ececec}

/* inspire */
.inspire{height:437px;background:var(--red);color:var(--white)}
.inspire .eyebrow{color:var(--white)}
.inspire .mark{background:var(--white)}
.inspire .heading{color:var(--white);font-size:34px}
.inspire .intro{position:absolute;left:656px;top:86px;width:317px;font-size:10px;line-height:20px;color:#fde3e5}
.service-card{position:absolute;top:230px;width:238px;height:131px;background:var(--white);color:var(--ink)}
.service-card h3{position:absolute;left:24px;top:24px;width:120px;font-size:11px;line-height:14px;font-weight:700}
.service-card p{position:absolute;left:24px;top:60px;width:108px;font-size:8px;line-height:14px;color:var(--muted)}
.service-card .photo{right:0;top:0;width:94px;height:131px}

/* trusted */
.trusted{height:426px;overflow:hidden}
.trusted-photo{inset:0;background:linear-gradient(90deg,#2c3246,#454c62 30%,#3a4258 55%,#5a6178 80%,#323950)}
.trusted .eyebrow{color:var(--yellow)}
.trusted .heading{color:var(--white);font-size:36px;line-height:46px}
.trusted .btn{left:539px;top:232px;width:122px;height:40px;font-size:10px}

/* contact + cases */
.reach{height:1120px}
.form-card{position:absolute;left:228px;top:-75px;width:745px;height:520px;background:var(--white);box-shadow:0 10px 40px rgba(0,0,0,.08)}
.form-card .heading{left:78px;top:118px;font-size:34px}
.field{position:absolute;height:40px;background:var(--field);font-size:9px;color:var(--muted);padding:12px 18px}
.call-panel{position:absolute;right:0;top:0;width:166px;height:520px;background:var(--red)}
.call-panel .vert{position:absolute;left:70px;top:50px;writing-mode:vertical-rl;font-family:"Caveat",cursive;font-size:15px;color:var(--white)}
.call-panel .ring{position:absolute;left:58px;top:222px;width:50px;height:50px;border:2px solid var(--white);border-radius:50%;display:flex;align-items:center;justify-content:center}
.call-panel .num{position:absolute;left:62px;top:295px;writing-mode:vertical-rl;font-size:30px;font-weight:600;color:var(--yellow);letter-spacing:1px}
.case-photo{top:673px;width:362px;height:300px}
.case-box{position:absolute;top:875px;width:212px;height:165px;padding:42px 0 0 78px}
.case-box h3{font-size:16px;line-height:19px;font-weight:600}
.case-box span{display:block;margin-top:18px;font-size:7px;font-weight:700;letter-spacing:1px}
.case-box .glyph{position:absolute;left:30px;top:44px}

/* testimonials */
.voices{height:673px;background:var(--gray-bg)}
.quote-card{position:absolute;top:231px;width:236px;height:319px;background:var(--white);text-align:center}
.quote-card .q{width:24px;height:24px;border-radius:50%;background:#f2f2f2;margin:38px auto 0;color:var(--muted);font-size:14px;line-height:28px}
.quote-card.mid .q{background:var(--red);color:var(--white)}
.quote-card p{margin:16px 28px 0;font-size:9.5px;line-height:20px;color:var(--muted)}
.avatar{width:36px;height:36px;border-radius:50%;background:#9aa3b4;margin:20px auto 0}
.quote-card .name{margin-top:6px;font-size:10px;font-weight:600}
.quote-card .role{font-size:8px;color:var(--muted)}
.corner{position:absolute;top:0;width:6px;height:6px;background:var(--red)}
.dots{position:absolute;left:587px;top:587px;display:flex;gap:5px}
.dots i{width:6px;height:6px;border-radius:50%;background:#c8c8c8}
.dots i:first-child{background:var(--navy)}

/* promise */
.promise{height:332px;background:var(--red)}
.promise .eyebrow{color:var(--white)}
.promise .mark{background:var(--white)}
.promise .heading{left:228px;top:128px;font-size:25px;line-height:30px;color:var(--white);letter-spacing:.3px}
.pledge{position:absolute;left:643px;width:330px;height:51px;background:var(--red-dark);display:flex;align-items:center;gap:14px;padding-left:18px;font-size:9.5px;font-weight:600;color:var(--white)}
.tick{width:24px;height:24px;border-radius:50%;background:var(--yellow);display:flex;align-items:center;justify-content:center}

/* helping */
.helping{height:691px;background:linear-gradient(180deg,var(--gray-bg) 303px,var(--white) 303px)}
.tab{position:absolute;top:241px;width:248px;height:56px;display:flex;align-items:center;justify-content:center;font-size:10px;font-weight:600}
.handshake-photo{left:228px;top:362px;width:319px;height:250px;background:linear-gradient(120deg,#eaeef3,#9aa3ae 40%,#c9d0d8 70%,#5a6070)}
.help-text{position:absolute;left:608px;top:356px;width:365px}
.help-text .p1{margin-left:64px;font-size:9.5px;line-height:20px;color:var(--muted)}
.help-text .p2{margin-top:14px;font-size:9.5px;line-height:20px;color:var(--muted)}
.help-text .link{margin-top:18px;font-size:9.5px;color:var(--red)}
.help-text .link+.link{margin-top:12px}
.help-text .glyph{position:absolute;left:0;top:4px}

/* start */
.start{height:367px;overflow:hidden}
.crowd-photo{inset:0;background:linear-gradient(180deg,#fff 0%,#f3f1ef 55%,#e9e4df 100%)}
.start .heading{line-height:42px}
.start .btn{left:539px;top:246px;width:122px;height:40px;font-size:10px}

/* footer */
.site-footer{height:405px;background:var(--navy);color:var(--white)}
.foot-brand{position:absolute;left:266px;top:30px;display:flex;flex-direction:column;align-items:center;gap:8px;font-size:14px;font-weight:500;letter-spacing:1px}
.foot-brand i{width:34px;height:34px;border:2px solid var(--white);display:block}
.foot-about{position:absolute;left:228px;top:113px;width:240px;font-size:8.5px;line-height:17px;color:#aeb2bf}
.subscribe{position:absolute;left:228px;top:191px;display:flex}
.subscribe div{width:200px;height:38px;background:var(--white);font-size:8.5px;color:var(--muted);padding:12px 16px}
.subscribe b{width:36px;height:38px;background:var(--red);display:flex;align-items:center;justify-content:center}
.foot-title{position:absolute;top:76px;font-size:11px;font-weight:600}
.foot-links{position:absolute;top:112px;list-style:none;font-size:8.5px;line-height:25px;color:#aeb2bf}
.foot-links .on{color:var(--yellow)}
.foot-contact{position:absolute;left:799px;top:110px;width:200px}
.foot-contact .row{display:flex;gap:10px;margin-bottom:10px}
.foot-contact .lab{font-size:8px;color:#aeb2bf;line-height:13px}
.foot-contact .val{font-size:8.5px;font-weight:600;line-height:15px}
.socials{position:absolute;top:358px;left:780px;display:flex;gap:38px;font-size:8px;font-weight:600;letter-spacing:1px;color:#aeb2bf}
.socials span:first-child{color:var(--yellow)}
</style>
</head>
<body>
<div class="page">

  <header class="topbar">
    <div class="brand"><span class="brand-square"></span>MARBECK PARTNERS</div>
    <div class="btn red" style="left:359px;top:27px;width:90px;height:32px;font-size:9px">Get Started</div>
    <div class="contact-item" style="left:498px">
      <span class="icon-dot"><svg width="12" height="10" viewBox="0 0 12 10"><rect x=".5" y=".5" width="11" height="9" fill="none" stroke="#fff"/><path d="M.5 .5 6 5l5.5-4.5" fill="none" stroke="#fff"/></svg></span>
      <div><div class="lab">Email</div><div class="val">hello@marbeckpartners.com</div></div>
    </div>
    <div class="contact-item" style="left:680px">
      <span class="icon-dot"><svg width="12" height="12" viewBox="0 0 12 12"><path d="M2 1h3l1 3-2 1a7 7 0 0 0 3 3l1-2 3 1v3c-6 0-10-4-10-9z" fill="#fff"/></svg></span>
      <div><div class="lab">Phone</div><div class="val">+1 555 014 2290</div></div>
    </div>
    <div class="contact-item" style="left:809px">
      <span class="icon-dot"><svg width="10" height="13" viewBox="0 0 10 13"><path d="M5 0a5 5 0 0 0-5 5c0 4 5 8 5 8s5-4 5-8a5 5 0 0 0-5-5z" fill="#fff"/><circle cx="5" cy="5" r="1.8" fill="#e84c56"/></svg></span>
      <div><div class="lab">Address</div><div class="val">48 Harrow Lane, Easton, USA</div></div>
    </div>
  </header>

  <nav class="mainnav">
    <ul>
      <li class="active">Home</li><li>About us</li><li>Services ▾</li><li>Industries ▾</li><li>Our success</li><li>Contact</li>
    </ul>
    <div class="lang"><i></i>English ▾</div>
  </nav>

  <section class="hero">
    <div class="photo hero-photo" role="img" aria-label="Sunlit beach with turquoise sea and a person relaxing on the sand"></div>
    <h1>DOES YOUR BUSINESS<br>HAVE AN EXIT PLAN?</h1>
    <p class="lead">Let us help you with a completely impartial, no obligation assessment</p>
    <a class="btn red">Contact Us</a>
  </section>

  <section class="mission">
    <span class="mark center" style="top:68px"></span>
    <p class="eyebrow center" style="top:82px">Our To Do Well</p>
    <h2 class="heading center" style="top:120px;font-size:30px;line-height:36px">Our Missions is to Give You<br>The Best Business Exit Plan</h2>
    <div class="photo team-photo" role="img" aria-label="Team of advisors in discussion around a meeting table"></div>
    <div class="commit-card"><p>We're committed to trusted financial advisors</p><span>READ MORE</span></div>

    <span class="mark" style="left:232px;top:660px"></span>
    <p class="eyebrow" style="left:228px;top:674px">Discover</p>
    <h2 class="heading" style="left:222px;top:702px;font-size:29px;line-height:35px;letter-spacing:.3px">Give You Business<br>The Best Exit Ever</h2>
    <div class="photo office-photo" role="img" aria-label="Colleagues reviewing work together at an office desk"></div>

    <div class="solutions">
      <div class="sol-head">–&nbsp; Solutions for small and large businesses</div>
      <p class="sol-body">We review your numbers, market position and goals, then map a clear route to a sale or handover. Every plan is built around your timeline and what you want next.</p>
      <div class="sol-row"><b>+</b>We can help your business to grow</div>
      <div class="sol-row"><b>+</b>Best financial and consultancy advisors</div>
      <div class="sol-row"><b>+</b>We only choose the best one for you</div>
    </div>
    <div class="rule"></div>
  </section>

  <section class="inspire">
    <span class="mark" style="left:232px;top:78px"></span>
    <p class="eyebrow" style="left:228px;top:92px">Explore Consulting Services</p>
    <h2 class="heading" style="left:228px;top:115px">We inspire and help<br>our customers</h2>
    <p class="intro">Owners who plan early sell for more. We guide you through valuation, preparation and buyer search so you can step away on your own terms, with nothing left to chance.</p>
    <div class="service-card" style="left:228px"><h3>Our Business Growth</h3><p>Steady advice to grow value before you sell.</p><div class="photo" role="img" aria-label="Advisor smiling at a desk" style="background:linear-gradient(160deg,#d7cfc6,#7d6a5d)"></div></div>
    <div class="service-card" style="left:482px"><h3>Finance Advice Solution</h3><p>Clear numbers that buyers trust and value.</p><div class="photo" role="img" aria-label="Consultant working on a laptop" style="background:linear-gradient(160deg,#d3dae3,#6b7c90)"></div></div>
    <div class="service-card" style="left:735px"><h3>Top-Notch Consultation</h3><p>Senior guidance at every step of your exit.</p><div class="photo" role="img" aria-label="Two colleagues talking in an office" style="background:linear-gradient(160deg,#e4e6ea,#8a8f9a)"></div></div>
  </section>

  <section class="trusted">
    <div class="photo trusted-photo" role="img" aria-label="Business meeting scene under a dark overlay"></div>
    <p class="eyebrow center" style="top:72px">Finance And Consulting Business</p>
    <h2 class="heading center" style="top:98px">Trusted &amp; professional<br>advisors for your business</h2>
    <a class="btn white">Get Started</a>
  </section>

  <section class="reach">
    <div class="form-card">
      <span class="mark" style="left:82px;top:72px"></span>
      <p class="eyebrow" style="left:78px;top:86px">Contact Now</p>
      <h2 class="heading">Feel free to make a<br>call request now</h2>
      <div class="field" style="left:78px;top:237px;width:204px">Business planning</div>
      <div class="field" style="left:78px;top:291px;width:204px">Your name</div>
      <div class="field" style="left:78px;top:345px;width:204px">Email address</div>
      <div class="field" style="left:78px;top:399px;width:204px">Phone number</div>
      <div class="field" style="left:297px;top:237px;width:204px;height:148px">Write message</div>
      <div class="btn red" style="left:297px;top:399px;width:122px;height:40px;font-size:9px">Get Started</div>
      <div class="call-panel">
        <p class="vert">For any inquiries call now</p>
        <div class="ring"><svg width="20" height="20" viewBox="0 0 12 12"><path d="M2 1h3l1 3-2 1a7 7 0 0 0 3 3l1-2 3 1v3c-6 0-10-4-10-9z" fill="none" stroke="#fff" stroke-width=".8"/></svg></div>
        <p class="num">800 555 0199</p>
      </div>
    </div>

    <span class="mark center" style="top:522px"></span>
    <p class="eyebrow center" style="top:536px">Our Recent Work</p>
    <h2 class="heading center" style="top:560px">Take a look at our<br>recent cases</h2>
    <div class="photo case-photo" role="img" aria-label="Team gathered around a table reviewing plans" style="left:228px;background:linear-gradient(135deg,#cdd6e2,#8493a8 50%,#d9c6bd)"></div>
    <div class="photo case-photo" role="img" aria-label="Two colleagues in thoughtful conversation" style="left:611px;background:linear-gradient(135deg,#b8b2ab,#6f6d70 55%,#c9ccd2)"></div>
    <div class="case-box" style="left:389px;background:var(--white)">
      <svg class="glyph" width="30" height="30" viewBox="0 0 30 30"><rect x="3" y="6" width="22" height="18" fill="none" stroke="#e84c56" stroke-width="1.5"/><path d="M7 20l5-6 4 3 6-8" fill="none" stroke="#e84c56" stroke-width="1.5"/></svg>
      <h3>Financial<br>Marketing<br>Advice</h3><span style="color:var(--red)">READ MORE</span>
    </div>
    <div class="case-box" style="left:761px;background:var(--red);color:var(--white)">
      <svg class="glyph" width="30" height="30" viewBox="0 0 30 30"><circle cx="13" cy="13" r="8" fill="none" stroke="#f7e14a" stroke-width="1.5"/><path d="M19 19l7 7" stroke="#f7e14a" stroke-width="2"/></svg>
      <h3>Research<br>Beyond the<br>Business</h3><span>READ MORE</span>
    </div>
  </section>

  <section class="voices">
    <span class="mark center" style="top:78px"></span>
    <p class="eyebrow center" style="top:92px">Our Testimonials</p>
    <h2 class="heading center" style="top:115px">What they are talking<br>about us</h2>
    <div class="quote-card" style="left:228px"><span class="corner" style="left:0;background:var(--yellow)"></span><div class="q">"</div><p>I was impressed by the advice and support. The team kept the sale on track and made a hard choice much easier.</p><div class="avatar" role="img" aria-label="Client portrait"></div><div class="name">Nora Vale</div><div class="role">Customer</div></div>
    <div class="quote-card mid" style="left:482px"><div class="q">"</div><p>I was impressed by the advice and support. The team kept the sale on track and made a hard choice much easier.</p><div class="avatar" role="img" aria-label="Client portrait"></div><div class="name">Daniel Price</div><div class="role">Customer</div></div>
    <div class="quote-card" style="left:737px"><span class="corner" style="right:0"></span><div class="q">"</div><p>I was impressed by the advice and support. The team kept the sale on track and made a hard choice much easier.</p><div class="avatar" role="img" aria-label="Client portrait"></div><div class="name">Leah Morton</div><div class="role">Customer</div></div>
    <div class="dots"><i></i><i></i><i></i></div>
  </section>

  <section class="promise">
    <span class="mark" style="left:232px;top:78px"></span>
    <p class="eyebrow" style="left:228px;top:92px">Get A Professional Advice</p>
    <h2 class="heading">Think Ahead And Prepare<br>The Best Exit Plan For Your<br>Business</h2>
    <div class="pledge" style="top:80px"><span class="tick"><svg width="12" height="10" viewBox="0 0 12 10"><path d="M1 5l3.5 3.5L11 1" fill="none" stroke="#e84c56" stroke-width="2"/></svg></span>We promise to respect your time</div>
    <div class="pledge" style="top:140px"><span class="tick"><svg width="12" height="10" viewBox="0 0 12 10"><path d="M1 5l3.5 3.5L11 1" fill="none" stroke="#e84c56" stroke-width="2"/></svg></span>We hire only professionals you can trust</div>
    <div class="pledge" style="top:200px"><span class="tick"><svg width="12" height="10" viewBox="0 0 12 10"><path d="M1 5l3.5 3.5L11 1" fill="none" stroke="#e84c56" stroke-width="2"/></svg></span>We promise to provide up front pricing</div>
  </section>

  <section class="helping">
    <span class="mark center" style="top:78px"></span>
    <p class="eyebrow center" style="top:92px">Customer Experience</p>
    <h2 class="heading center" style="top:115px">Helping you every step<br>of the way</h2>
    <div class="tab" style="left:228px;background:var(--white)">Business Growth</div>
    <div class="tab" style="left:476px;background:var(--red);color:var(--white)">Financial Advice</div>
    <div class="tab" style="left:724px;width:249px;background:var(--navy);color:var(--white)">Gobal Solutions</div>
    <div class="photo handshake-photo" role="img" aria-label="Business people shaking hands in a bright office"></div>
    <div class="help-text">
      <svg class="glyph" width="40" height="44" viewBox="0 0 40 44"><rect x="4" y="22" width="6" height="18" fill="none" stroke="#e84c56" stroke-width="1.5"/><rect x="16" y="14" width="6" height="26" fill="none" stroke="#e84c56" stroke-width="1.5"/><rect x="28" y="6" width="6" height="34" fill="none" stroke="#e84c56" stroke-width="1.5"/></svg>
      <p class="p1">A good exit starts long before a buyer appears. We look at the whole picture and help you fix weak spots so your business is ready when the time comes.</p>
      <p class="p2">If you are thinking about selling, talk to us early. There is no cost to find out where you stand today.</p>
      <p class="link">Solution for small and large type businesses</p>
      <p class="link">We can help your business to grow</p>
      <p class="link">Best financial and consulting services</p>
    </div>
  </section>

  <section class="start">
    <div class="photo crowd-photo" role="img" aria-label="Faded crowd of smiling clients"></div>
    <p class="eyebrow center" style="top:90px">We're Professional And Expert Consultants</p>
    <h2 class="heading center" style="top:114px">For better help and<br>business. Let's get started</h2>
    <a class="btn red">Get Started</a>
  </section>

  <footer class="site-footer">
    <div class="foot-brand"><i></i>MARBECK PARTNERS</div>
    <p class="foot-about">We help owners plan, prepare and complete the sale of their business with care and full discretion.</p>
    <div class="subscribe"><div>Email address</div><b><svg width="12" height="10" viewBox="0 0 12 10"><rect x=".5" y=".5" width="11" height="9" fill="none" stroke="#fff"/><path d="M.5 .5 6 5l5.5-4.5" fill="none" stroke="#fff"/></svg></b></div>
    <p class="foot-title" style="left:496px">Explore Marbeck</p>
    <ul class="foot-links" style="left:501px"><li>About</li><li class="on">Services</li><li>Careers</li><li>Our Team</li><li>Approach</li><li>Case Studies</li></ul>
    <ul class="foot-links" style="left:608px"><li>Locations</li><li>Clients</li><li>Help</li><li>Contact</li></ul>
    <ul class="foot-links" style="left:697px"><li>Privacy Policy</li><li>Terms of Use</li><li>Support</li></ul>
    <p class="foot-title" style="left:799px">Have any Question?</p>
    <div class="foot-contact">
      <div class="row"><svg width="10" height="10" viewBox="0 0 12 12"><path d="M2 1h3l1 3-2 1a7 7 0 0 0 3 3l1-2 3 1v3c-6 0-10-4-10-9z" fill="none" stroke="#f7e14a"/></svg><div><div class="lab">Phone</div><div class="val">+1 555 014 2290</div></div></div>
      <div class="row"><svg width="10" height="12" viewBox="0 0 10 13"><path d="M5 1a4 4 0 0 0-4 4c0 3 4 7 4 7s4-4 4-7a4 4 0 0 0-4-4z" fill="none" stroke="#f7e14a"/></svg><div><div class="lab">Address</div><div class="val">48 Harrow Lane,<br>Easton, USA</div></div></div>
      <div class="row"><svg width="11" height="9" viewBox="0 0 12 10"><rect x=".5" y=".5" width="11" height="9" fill="none" stroke="#f7e14a"/><path d="M.5 .5 6 5l5.5-4.5" fill="none" stroke="#f7e14a"/></svg><div><div class="lab">Email</div><div class="val">help@marbeckpartners.com</div></div></div>
    </div>
    <div class="socials"><span>NEWS FEED</span><span>COMMUNITY</span><span>NETWORK</span></div>
  </footer>

</div>
</body>
</html>
```